business card for real estate company

I need a sharp creative business card design that stands out for a real estate company that does the following
- Selling land
- Selling houses and apartments
- Property management

website www.velmarkestates.com
email: info at the above web address
phone number place holder

```html
<!DOCTYPE html>
<html lang="en">
<head>
<meta charset="utf-8">
<title>Velmark Estates – Business Card</title>
<link rel="stylesheet" href="https://fonts.googleapis.com/css2?family=Lato:wght@400;700&family=Roboto:wght@500&display=swap">
<style>
  :root {
    --navy: #0e1324;
    --green: #5db533;
    --white: #ffffff;
    --muted: #e4e6ea;
    --stage: #eef0f3;
    --sky: #7f93ad;
    --facade: #c9b79a;
    --lawn: #8a7657;
  }
  * { box-sizing: border-box; margin: 0; padding: 0; }
  html, body { width: 1200px; height: 1200px; overflow: hidden; }
  body { background: var(--stage); position: relative; font-family: "Lato", sans-serif; }

  .card {
    position: absolute;
    top: 216px;
    width: 437px;
    height: 768px;
    border-radius: 27px;
    overflow: hidden;
    background: var(--navy);
  }
  .card--front { left: 123px; }
  .card--back { left: 637px; }

  .card__photo {
    position: absolute; left: 0; top: 0; width: 100%; height: 287px;
    background: linear-gradient(180deg, var(--sky) 0%, #a9b4c0 30%, var(--facade) 55%, #b9a88c 78%, var(--lawn) 100%);
  }

  .brand {
    position: absolute; left: 0; width: 100%;
    text-align: center;
    font-family: "Lato", sans-serif;
    font-weight: 700;
    text-transform: uppercase;
    line-height: 1.05;
  }
  .brand__mark {
    display: block; width: 22px; height: 22px; margin: 0 auto 14px;
    border-radius: 50%;
  }
  .brand__name { display: block; font-size: 52px; letter-spacing: 1px; }
  .brand__sub { display: block; font-size: 52px; letter-spacing: 1px; }

  .card--front .brand { top: 380px; color: var(--white); }
  .card--front .brand__mark { background: var(--green); }

  .services {
    position: absolute; left: 41px; top: 584px;
    list-style: none;
    font-family: "Roboto", sans-serif; font-weight: 500;
    font-size: 21px; color: var(--green);
  }
  .services li { display: flex; align-items: center; gap: 8px; height: 34px; }
  .services svg { width: 21px; height: 21px; flex: none; }

  .card__top {
    position: absolute; left: 0; top: 0; width: 100%; height: 337px;
    background: var(--white);
  }
  .card--back .brand { top: 92px; color: var(--navy); }
  .card--back .brand__mark { background: var(--green); }

  .person { position: absolute; left: 0; width: 100%; text-align: center; }
  .person__name { top: 403px; font-size: 37px; font-weight: 700; color: var(--green); }
  .person__role { top: 455px; font-size: 21px; font-weight: 700; color: var(--muted); }

  .contact-icons {
    position: absolute; top: 501px; left: 0; width: 100%;
    display: flex; justify-content: center; gap: 12px;
  }
  .contact-icons span {
    width: 24px; height: 24px; border-radius: 5px; background: var(--white);
    display: flex; align-items: center; justify-content: center;
  }
  .contact-icons svg { width: 16px; height: 16px; }

  .contact {
    position: absolute; top: 549px; left: 0; width: 100%;
    list-style: none; text-align: center;
    font-size: 22px; line-height: 36px; color: var(--muted);
  }
</style>
</head>
<body>

<section class="card card--front">
  <div class="card__photo" role="img" aria-label="Photograph of a two-storey suburban house with a white garage door and front lawn"></div>
  <div class="brand">
    <span class="brand__mark"></span>
    <span class="brand__name">Velmark</span>
    <span class="brand__sub">Estates</span>
  </div>
  <ul class="services">
    <li><svg viewBox="0 0 24 24" fill="none" stroke="currentColor" stroke-width="2"><circle cx="12" cy="12" r="10"/><path d="M7.5 12.5l3 3 6-6.5"/></svg>Selling Land</li>
    <li><svg viewBox="0 0 24 24" fill="none" stroke="currentColor" stroke-width="2"><circle cx="12" cy="12" r="10"/><path d="M7.5 12.5l3 3 6-6.5"/></svg>Property Management</li>
    <li><svg viewBox="0 0 24 24" fill="none" stroke="currentColor" stroke-width="2"><circle cx="12" cy="12" r="10"/><path d="M7.5 12.5l3 3 6-6.5"/></svg>Selling Houses and Apartments</li>
  </ul>
</section>

<section class="card card--back">
  <div class="card__top"></div>
  <div class="brand">
    <span class="brand__mark"></span>
    <span class="brand__name">Velmark</span>
    <span class="brand__sub">Estates</span>
  </div>

  <p class="person person__name">Daniel Okoth</p>
  <p class="person person__role">Founder</p>

  <div class="contact-icons">
    <span><svg viewBox="0 0 16 16" fill="none" stroke="#0e1324" stroke-width="1.6"><rect x="4.5" y="1.5" width="7" height="13" rx="1.5"/><path d="M7 12.3h2"/></svg></span>
    <span><svg viewBox="0 0 16 16" fill="#0e1324"><path d="M14.5 1.5L1.5 7l5 1.8 1.8 5.2z"/></svg></span>
    <span><svg viewBox="0 0 16 16" fill="none" stroke="#0e1324" stroke-width="1.4"><circle cx="8" cy="8" r="6.2"/><ellipse cx="8" cy="8" rx="2.6" ry="6.2"/><path d="M1.8 8h12.4"/></svg></span>
    <span><svg viewBox="0 0 16 16" fill="#0e1324"><path d="M8 1a4.8 4.8 0 0 0-4.8 4.8C3.2 9.6 8 15 8 15s4.8-5.4 4.8-9.2A4.8 4.8 0 0 0 8 1zm0 6.6a1.8 1.8 0 1 1 0-3.6 1.8 1.8 0 0 1 0 3.6z"/></svg></span>
  </div>

  <ul class="contact">
    <li>+254 712 555 019</li>
    <li>www.velmarkestates.com</li>
    <li>info@velmarkestates.com</li>
    <li>Nairobi, Kenya</li>
  </ul>
</section>

</body>
</html>
```